Business Card - Rebranding for Consulting Firm

We are renaming and rebranding our consulting firm and need to raise the level of quality of our cards as part of that effort. We consult to leading high tech, life science and other innovation sector companies.

Need a two-sided business card design.

Side 1: (a) Company logo (b) tag line: Get More From the People You Hire (c) Name (d) Title (e) Phone 1: Office (f) Phone 2: Mobile (g) email: person@HollowmereAdvisory.com

Side 2: Two lines of text: (a) Markets Shift Quickly. Teams Must Adapt. People Deliver the Plan. (b) We help you lead through each one.

Target Market(s)

Business and human resources executives and senior managers

Industry/Entity Type

Management Consulting

Contact Information for Business Card

Font styles to use
Sans Serif

Requirements
Must have
• clean, not too busy, but with a bit of creativity. Stick to the colors used in the attached logo
• appeal to high tech, life science companies
Nice to have
• prefer white background

```html
<!DOCTYPE html>
<html lang="en">
<head>
<meta charset="utf-8">
<title>Hollowmere Advisory – Business Card</title>
<link href="https://fonts.googleapis.com/css2?family=Lato:ital,wght@0,400;0,700;0,900;1,400&display=swap" rel="stylesheet">
<style>
  :root {
    --brand-blue: #0d5f9e;
    --brand-blue-light: #0a7fc4;
    --brand-cyan: #1a9ad6;
    --ink-grey: #6b6f74;
    --paper: #ffffff;
    --backdrop: #e9eaec;
  }
  * { margin: 0; padding: 0; box-sizing: border-box; }
  html, body {
    width: 1200px; height: 837px; overflow: hidden;
    background: var(--backdrop);
    font-family: "Lato", sans-serif;
  }
  .sheet {
    width: 1200px; height: 837px;
    display: flex; align-items: center; justify-content: center; gap: 40px;
  }
  .card {
    width: 520px; height: 297px;
    position: relative;
    box-shadow: 0 6px 18px rgba(0,0,0,0.12);
  }

  /* Front side */
  .card-front { background: var(--paper); }
  .brand {
    position: absolute; left: 48px; top: 54px;
    display: flex; align-items: center; gap: 12px;
  }
  .brand-square {
    width: 30px; height: 30px; background: var(--brand-blue-light); flex: none;
  }
  .brand-name {
    font-weight: 700; font-size: 34px; letter-spacing: -0.5px;
    color: var(--brand-blue); white-space: nowrap;
  }
  .tagline {
    position: absolute; left: 48px; top: 104px;
    font-style: italic; font-size: 15px; color: var(--brand-cyan);
  }
  .contact {
    position: absolute; left: 280px; top: 170px;
  }
  .contact-name {
    font-weight: 900; font-size: 17px; letter-spacing: 0.5px;
    color: var(--brand-blue); text-transform: uppercase;
  }
  .contact-title {
    font-size: 13px; color: var(--ink-grey); margin-bottom: 10px;
  }
  .contact-line {
    display: flex; align-items: center; gap: 8px;
    font-size: 12.5px; color: var(--ink-grey); line-height: 20px;
    white-space: nowrap;
  }
  .contact-icon { width: 14px; height: 14px; flex: none; }

  /* Back side */
  .card-back {
    background: linear-gradient(120deg, var(--brand-blue) 0%, var(--brand-blue-light) 100%);
    color: var(--paper);
    display: flex; flex-direction: column; align-items: center; justify-content: center;
    text-align: center;
  }
  .card-back .brand-row { display: flex; align-items: center; gap: 12px; margin-bottom: 22px; }
  .card-back .brand-square { background: var(--paper); }
  .card-back .brand-name { color: var(--paper); font-size: 36px; }
  .statement { font-size: 14px; line-height: 22px; }
</style>
</head>
<body>
<main class="sheet">

  <section class="card card-front" aria-label="Business card front">
    <div class="brand">
      <span class="brand-square"></span>
      <span class="brand-name">Hollowmere Advisory</span>
    </div>
    <p class="tagline">Get More From the People You Hire</p>

    <div class="contact">
      <p class="contact-name">Dana Reyes</p>
      <p class="contact-title">Director</p>
      <p class="contact-line">
        <svg class="contact-icon" viewBox="0 0 14 14" aria-hidden="true">
          <rect width="14" height="14" rx="2" fill="#0d5f9e"/>
          <path d="M4 3.5c.6-.4 1.2-.3 1.5.3l.6 1.2c.2.4 0 .8-.3 1l-.4.3c.4.9 1.1 1.6 2 2l.3-.4c.2-.3.6-.5 1-.3l1.2.6c.6.3.7.9.3 1.5-.5.7-1.2.9-2 .6C6.3 9.6 4.4 7.7 3.7 5.6c-.3-.8-.1-1.5.3-2.1z" fill="#fff"/>
        </svg>
        (01) 5550 0142
      </p>
      <p class="contact-line">
        <svg class="contact-icon" viewBox="0 0 14 14" aria-hidden="true">
          <rect width="14" height="14" rx="2" fill="#0d5f9e"/>
          <rect x="4.5" y="2.5" width="5" height="9" rx="1" fill="none" stroke="#fff" stroke-width="1.2"/>
          <circle cx="7" cy="10" r="0.6" fill="#fff"/>
        </svg>
        (01) 5550 0142
      </p>
      <p class="contact-line">
        <svg class="contact-icon" viewBox="0 0 14 14" aria-hidden="true">
          <rect width="14" height="14" rx="2" fill="#0d5f9e"/>
          <rect x="2.5" y="4" width="9" height="6" fill="none" stroke="#fff" stroke-width="1.1"/>
          <path d="M2.5 4l4.5 3.5L11.5 4" fill="none" stroke="#fff" stroke-width="1.1"/>
        </svg>
        person@HollowmereAdvisory.com
      </p>
    </div>
  </section>

  <section class="card card-back" aria-label="Business card back">
    <div class="brand-row">
      <span class="brand-square"></span>
      <span class="brand-name">Hollowmere Advisory</span>
    </div>
    <p class="statement">Markets Shift Quickly. Teams Must Adapt. People Deliver the Plan.</p>
    <p class="statement">We help you lead through each one.</p>
  </section>

</main>
</body>
</html>
```